PENNIMARTEL & PENNIMARTEL,LLP NEEDS A NEW LETTERHEAD DESIGN

a conservative yet contemporary layout befitting a long established
firm, consistent with the times, some form of logo so it catches ones attention, and is
admirable, but portrays integrity
Updates

I would like to approve #22066987 Please advise how to do this as it’s confusing on the site so I can approve payment for the designer

Target Market(s)

real estate investors and building management people

Industry/Entity Type

Law Firm

Font styles to use
Serif

Colors

Designer to choose colors to be used in the design.

Requirements
Must have
• some form of conservative logo

```html
<!DOCTYPE html>
<html lang="en">
<head>
<meta charset="utf-8">
<title>Pennimartel &amp; Pennimartel, LLP — Letterhead</title>
<link rel="stylesheet" href="https://fonts.googleapis.com/css2?family=Questrial&display=swap">
<style>
  :root {
    --backdrop: #c9cacf;
    --paper: #f2f2f2;
    --ink: #8a8d96;
    --ink-strong: #7d808a;
    --band: #8f939c;
  }
  * { margin: 0; padding: 0; box-sizing: border-box; }
  html, body {
    width: 1200px;
    height: 1166px;
    overflow: hidden;
    background: var(--backdrop);
  }
  .sheet {
    position: absolute;
    left: 175px;
    top: 33px;
    width: 850px;
    height: 1100px;
    background: var(--paper);
    font-family: "Questrial", "Helvetica Neue", Arial, sans-serif;
    color: var(--ink);
  }
  .sheet__band {
    position: absolute;
    left: 0; top: 0;
    width: 100%;
    height: 7px;
    background: var(--band);
  }
  .masthead {
    position: absolute;
    left: 63px;
    top: 64px;
    display: flex;
    align-items: flex-start;
    gap: 20px;
  }
  .masthead__name {
    font-size: 21px;
    line-height: 22px;
    letter-spacing: 0.3px;
    color: var(--ink-strong);
    text-transform: uppercase;
  }
  .masthead__tagline {
    font-size: 13.5px;
    line-height: 15.5px;
    letter-spacing: 0.4px;
    text-align: right;
    text-transform: uppercase;
    padding-top: 1px;
  }
  .footer {
    position: absolute;
    left: 63px;
    right: 61px;
    top: 1024px;
    display: flex;
    align-items: center;
    font-size: 10.2px;
    line-height: 14px;
    letter-spacing: 0.9px;
    text-transform: uppercase;
  }
  .footer__firm { width: 374px; }
  .footer__firm-name { color: var(--ink-strong); font-weight: 700; letter-spacing: 0.6px; }
  .footer__divider {
    width: 1px;
    height: 22px;
    background: var(--ink);
    opacity: 0.7;
  }
  .footer__phones { margin-left: 36px; width: 162px; }
  .footer__web { margin-left: 36px; }
</style>
</head>
<body>
  <main class="sheet">
    <div class="sheet__band"></div>

    <header class="masthead">
      <div class="masthead__name">Pennimartel &amp;<br>Pennimartel</div>
      <div class="masthead__tagline">Attorneys and<br>Counselors<br>at Law</div>
    </header>

    <footer class="footer">
      <div class="footer__firm">
        <div class="footer__firm-name">Pennimartel &amp; Pennimartel, LLP</div>
        <div>40 Alder Row Suite 210, Westbrook, New York 10990</div>
      </div>
      <span class="footer__divider"></span>
      <div class="footer__phones">
        <div>Tel: (555) 014-2231</div>
        <div>Fax: (555) 014-2290</div>
      </div>
      <span class="footer__divider"></span>
      <div class="footer__web">
        <div>info@pmlawgroup.com</div>
        <div>www.pmlawgroup.com</div>
      </div>
    </footer>
  </main>
</body>
</html>
```